Baby Organic Coconut Body Lotion

Meadow Crib Naturals is developing a line of Organic and Natural skin care products for babies and toddlers, although our skin care can also be used by adults too. These products include a body lotion, shampoo & body wash, powder, hair cream, massage body oil, bath soak, baby balm, Bar Soap, gift box and many more.
This will be an ever expanding line so the list will go on and on. We are looking forward for an eye catching designs. I attached some of our current label designs and product images. Also, we have different Baby organic body lotion and Baby organic shampoo & body wash with different fruit flavours. Coconut lotion will share the same design with the shampoo & body wash. I would like you to start with the coconut design. I have uploaded plastic bottles with different colourful caps. The bottle with the white cap is for the coconut design. the bottle with the red cap is for the strawberry design. the bottle with the orange cap is for the orange design. the bottle with the yellow cap is for the pineapple design. the bottle with the green cap is for the apple design. Bear in my mind that my baby organic skin care are made with different fruit flavours.
Target Market(s)
My target market are for mothers that wants to buy there baby and toddler skin care products.
Industry/Entity Type
Baby
Look and feel

```html
<!DOCTYPE html>
<html lang="en">
<head>
<meta charset="utf-8">
<title>Meadow Crib Naturals – Apple Labels</title>
<link rel="stylesheet" href="https://fonts.googleapis.com/css2?family=Antonio:wght@100&family=Jost:wght@300;700&display=swap">
<style>
  :root {
    --ink: #000000;
    --paper: #ffffff;
    --apple-red: #be1e2d;
  }
  html, body {
    margin: 0;
    padding: 0;
    overflow: hidden;
    background: var(--paper);
  }
  .canvas {
    position: relative;
    width: 1200px;
    height: 1000px;
    background: var(--paper);
    overflow: hidden;
  }
  .label {
    position: absolute;
    top: 0;
    width: 500px;
    height: 1000px;
  }
  .label--lotion { left: 87px; }
  .label--wash { left: 588px; }
  .brand-name {
    position: absolute;
    top: 115px;
    left: 0;
    width: 500px;
    margin: 0;
    text-align: center;
    font-family: "Antonio", "Oswald", sans-serif;
    font-weight: 100;
    color: var(--ink);
    line-height: 1;
  }
  .brand-name__big {
    display: block;
    font-size: 96px;
    letter-spacing: 6px;
    line-height: 96px;
  }
  .brand-name__small {
    display: block;
    font-size: 46px;
    letter-spacing: 2px;
    line-height: 56px;
    margin-top: 7px;
  }
  .badge {
    position: absolute;
    top: 395px;
    left: 71px;
    width: 360px;
    height: 490px;
  }
  .badge__product {
    font-family: "Jost", "Futura", sans-serif;
    font-weight: 700;
    font-size: 70px;
    fill: var(--ink);
  }
  .badge__type {
    font-family: "Jost", "Futura", sans-serif;
    font-weight: 300;
    font-size: 31px;
    letter-spacing: 4px;
    fill: var(--ink);
  }
  .badge__maker {
    font-family: "Jost", "Futura", sans-serif;
    font-weight: 300;
    font-size: 10px;
    letter-spacing: 1px;
    fill: var(--ink);
  }
  .rule { stroke: var(--ink); stroke-width: 2.5; }
</style>
</head>
<body>
<main class="canvas">

  <section class="label label--lotion">
    <h1 class="brand-name">
      <span class="brand-name__big">MEADOW</span>
      <span class="brand-name__small">CRIB</span>
      <span class="brand-name__big">NATURALS</span>
    </h1>
    <svg class="badge" viewBox="0 0 360 490" xmlns="http://www.w3.org/2000/svg">
      <polygon points="179,78 356,180 356,384 179,486 3,384 3,180" fill="var(--ink)"/>
      <polygon points="179,89 347,186 347,378 179,475 12,378 12,186" fill="var(--apple-red)"/>
      <polygon points="179,104 333,193 333,371 179,460 25,371 25,193" fill="var(--paper)"/>
      <rect role="img" aria-label="Red apple with green leaf illustration" x="85" y="30" width="192" height="185" rx="85" fill="var(--apple-red)"/>
      <polygon points="80,187 84.5,199 97,199 87,207 91,220 80,212 69,220 73,207 63,199 75.5,199" fill="var(--ink)"/>
      <polygon points="282,187 286.5,199 299,199 289,207 293,220 282,212 271,220 275,207 265,199 277.5,199" fill="var(--ink)"/>
      <line class="rule" x1="114" y1="232" x2="244" y2="232"/>
      <line class="rule" x1="37" y1="245" x2="322" y2="245"/>
      <text class="badge__product" x="179" y="307" text-anchor="middle">APPLE</text>
      <line class="rule" x1="37" y1="313" x2="322" y2="313"/>
      <line class="rule" x1="114" y1="326" x2="244" y2="326"/>
      <text class="badge__type" x="181" y="360" text-anchor="middle">BODY</text>
      <text class="badge__type" x="181" y="393" text-anchor="middle">LOTION</text>
      <text class="badge__maker" x="179" y="422" text-anchor="middle">MEADOW CRIB NATURALS</text>
    </svg>
  </section>

  <section class="label label--wash">
    <h1 class="brand-name">
      <span class="brand-name__big">MEADOW</span>
      <span class="brand-name__small">CRIB</span>
      <span class="brand-name__big">NATURALS</span>
    </h1>
    <svg class="badge" viewBox="0 0 360 490" xmlns="http://www.w3.org/2000/svg">
      <polygon points="179,78 356,180 356,384 179,486 3,384 3,180" fill="var(--ink)"/>
      <polygon points="179,89 347,186 347,378 179,475 12,378 12,186" fill="var(--apple-red)"/>
      <polygon points="179,104 333,193 333,371 179,460 25,371 25,193" fill="var(--paper)"/>
      <rect role="img" aria-label="Red apple with green leaf illustration" x="85" y="30" width="192" height="185" rx="85" fill="var(--apple-red)"/>
      <polygon points="80,187 84.5,199 97,199 87,207 91,220 80,212 69,220 73,207 63,199 75.5,199" fill="var(--ink)"/>
      <polygon points="282,187 286.5,199 299,199 289,207 293,220 282,212 271,220 275,207 265,199 277.5,199" fill="var(--ink)"/>
      <line class="rule" x1="114" y1="232" x2="244" y2="232"/>
      <line class="rule" x1="37" y1="245" x2="322" y2="245"/>
      <text class="badge__product" x="179" y="307" text-anchor="middle">APPLE</text>
      <line class="rule" x1="37" y1="313" x2="322" y2="313"/>
      <line class="rule" x1="114" y1="326" x2="244" y2="326"/>
      <text class="badge__type" x="181" y="360" text-anchor="middle">SHAMPOO+BODY</text>
      <text class="badge__type" x="181" y="393" text-anchor="middle">WASH</text>
      <text class="badge__maker" x="179" y="422" text-anchor="middle">MEADOW CRIB NATURALS</text>
    </svg>
  </section>

</main>
</body>
</html>
```